Microlight Aircraft Website Project

Need a website designed, or at least a template made, that my web programmer can work with here. We are a new manufacturer of microlight aircraft & powered hang gliders. Our company name is Brisk Tern. We manufacture portable utility aircraft in the Light Sport category (formerly known as Ultralights or Microlights). Our particular design is a 2-seat powered hang glider and caters to those who want to go explore the backcountry. We are not necessarily aviation nuts, but more into the development of a flying utility vehicle for extreme exploration and expeditions. We have been importing these aircraft from 3 countries for 15 years and have supplied over 200 expedition-quality aircraft world-wide. We are now manufacturing here in the US.

Industry/Entity Type

Manufacturer

Coding

Coded - Design and coding required

```html
<!DOCTYPE html>
<html lang="en">
<head>
<meta charset="utf-8">
<title>Brisk Tern — Light Sport Aircraft</title>
<link rel="stylesheet" href="https://fonts.googleapis.com/css2?family=Oswald:wght@400;500;600&family=Open+Sans:wght@400;600;700&display=swap">
<style>
:root{
  --blue:#1446d8;
  --navy:#0b2270;
  --navy-card:#0d2a8c;
  --cyan:#4ee0ee;
  --ink:#333;
  --muted:#555;
  --light:#f4f5f6;
  --white:#fff;
  --hero-dark:#1b1d20;
}
*{box-sizing:border-box;margin:0;padding:0}
html,body{width:1200px;height:2242px;overflow:hidden}
body{font-family:"Open Sans",Arial,sans-serif;color:var(--ink);background:var(--white);position:relative}
a{color:inherit;text-decoration:none}
.heading{font-family:"Oswald","Arial Narrow",sans-serif;font-weight:500;text-transform:uppercase}

/* top bar */
.top-bar{height:27px;background:var(--blue);color:var(--white);font-size:10px;display:flex;align-items:center;justify-content:space-between;padding:0 73px}
.top-bar .account{display:flex;gap:22px;align-items:center}
.top-bar .user{display:flex;gap:8px;align-items:center;text-transform:uppercase}

/* nav */
.site-nav{height:57px;background:var(--light);display:flex;align-items:center;justify-content:space-between;padding-left:65px;padding-right:52px}
.brand{display:flex;align-items:center;gap:10px;font-family:"Open Sans",sans-serif;font-weight:700;font-size:25px;color:var(--blue);text-transform:uppercase}
.brand .mark{width:28px;height:28px;border-radius:50%;background:var(--blue)}
.menu{display:flex;align-items:center;height:57px;font-size:12px;font-weight:600;color:var(--blue);text-transform:uppercase}
.menu .home{width:80px;height:57px;background:var(--cyan);display:flex;align-items:center;justify-content:center;margin-right:22px}
.menu a{padding:0 20px}
.menu .search{padding-left:18px}

/* hero */
.hero{position:relative;height:482px;background:radial-gradient(ellipse at 70% 60%,#6a6d72 0%,#3a3c40 35%,var(--hero-dark) 75%)}
.hero-content{position:absolute;left:0;right:0;top:140px;text-align:center;color:var(--white)}
.hero-title{font-size:46px;color:var(--cyan);letter-spacing:-.5px;line-height:1}
.hero-rule{width:600px;height:2px;background:var(--cyan);margin:10px auto 8px}
.hero-text{font-size:21px;line-height:26px}
.btn-outline{display:inline-block;margin-top:20px;border:1px solid var(--white);padding:9px 34px;font-size:14px;text-transform:uppercase}
.dots{position:absolute;left:0;right:0;display:flex;justify-content:center;gap:6px}
.hero .dots{bottom:16px}
.dot{width:12px;height:12px;border-radius:50%;border:2px solid var(--white)}
.dot.active{border-color:var(--cyan)}

/* categories */
.categories{display:flex;gap:27px;padding:29px 73px 0}
.cat-card{position:relative;width:333px;height:167px;overflow:hidden}
.cat-photo{position:absolute;inset:0}
.cat-photo.formerly{background:linear-gradient(160deg,#3d5570 0%,#c98a44 70%,#6b4b30 100%)}
.cat-photo.ultralights{background:linear-gradient(170deg,#6d9fd0 0%,#3c6c9c 60%,#2f4f55 100%)}
.cat-photo.microlights{background:linear-gradient(180deg,#5a9ad8 0%,#a8c8e8 60%,#e8eef4 100%)}
.cat-panel{position:absolute;inset:0;background:rgba(244,245,246,.96);clip-path:polygon(58% 0,100% 0,100% 100%,26% 100%)}
.cat-title{position:absolute;right:0;top:0;height:63px;width:160px;background:var(--blue);clip-path:polygon(22% 0,100% 0,100% 100%,0 100%);color:var(--white);font-size:23px;line-height:26px;text-align:right;padding:6px 8px 0 0}
.cat-text{position:absolute;right:10px;top:70px;width:150px;text-align:right;font-size:14px;line-height:18px;color:var(--muted)}
.cat-more{position:absolute;right:10px;bottom:12px;font-size:14px;color:var(--muted)}
.cat-more.active{color:var(--cyan)}
.intro{padding:18px 73px 0;font-size:16px;line-height:21px;text-align:center;color:var(--muted)}

/* offer */
.offer{position:absolute;top:890px;left:0;width:1200px;height:479px;background:var(--blue);color:var(--white);text-align:center}
.offer-title{font-size:38px;margin-top:30px;line-height:1}
.offer-lead{font-size:17px;line-height:21px;width:760px;margin:16px auto 0}
.offer-grid{display:flex;gap:5px;padding:0 73px;margin-top:18px}
.offer-card{flex:1;height:226px;background:var(--navy-card);padding:22px 22px 0}
.offer-card svg{width:56px;height:56px}
.offer-card h3{font-size:26px;color:var(--cyan);margin:6px 0 8px;line-height:1.1}
.offer-card p{font-size:15px;line-height:19px}
.btn-fill{display:inline-block;background:var(--cyan);color:var(--white);padding:9px 31px;font-size:14px;text-transform:uppercase;margin-top:34px}

/* testimonial */
.testimonial{position:absolute;top:1369px;left:0;width:1200px;height:346px;background:#f3f3f4;text-align:center}
.partner{margin-top:36px;font-family:"Oswald",sans-serif;font-weight:600;font-size:58px;color:var(--navy);text-transform:uppercase;line-height:1}
.quote{position:relative;width:600px;margin:24px auto 0;font-size:17px;line-height:22px;color:var(--ink)}
.quote-mark{position:absolute;font-family:Georgia,serif;font-weight:700;font-size:66px;line-height:1;color:var(--ink)}
.quote-mark.open{left:-46px;top:-10px}
.quote-mark.close{right:-46px;bottom:-40px}
.testimonial .dots{bottom:26px}
.testimonial .dot{border-color:#555}
.testimonial .dot.active{border-color:var(--cyan)}

/* bottom */
.bottom{position:absolute;top:1715px;left:73px;width:1055px;display:flex;gap:27px}
.col{width:333px}
.col-title{font-size:28px;color:var(--blue);line-height:1.2;margin-top:24px;padding-bottom:6px;border-bottom:2px solid #e3e5e8}
.news-photo{margin-top:28px;height:162px;background:linear-gradient(180deg,#6fa6d8 0%,#b8d4ee 55%,#eef2f6 100%)}
.news-text{margin-top:16px;font-size:15px;line-height:19px;color:var(--muted)}
.news-text strong{color:var(--blue);text-transform:uppercase}
.bottom .btn-fill{margin-top:22px;padding:9px 31px}
.post{display:flex;gap:10px;margin-top:24px}
.post + .post{margin-top:22px}
.post-side{width:54px;flex:none}
.avatar{height:54px;background:linear-gradient(180deg,#777 0%,#2b2b2b 100%)}
.date{background:var(--blue);color:var(--white);text-align:center;font-family:"Oswald",sans-serif;height:54px;padding-top:2px}
.date .m{font-size:18px;line-height:20px}
.date .d{font-size:28px;line-height:30px}
.post h4{font-family:"Oswald",sans-serif;font-size:17px;color:var(--blue);text-transform:uppercase;line-height:20px}
.post .by{font-size:11px;color:var(--ink);line-height:13px}
.post p{font-size:10px;line-height:13px;color:var(--muted);margin-top:4px}
.post .more{display:block;font-size:13px;color:var(--cyan);margin-top:10px}
.news-join{margin-top:22px;font-size:12px;font-weight:600;text-transform:uppercase}
.news-join span{color:var(--blue)}
.news-small{font-size:10px;line-height:13px;color:var(--muted);margin-top:4px}
.signup{display:flex;margin-top:18px;height:27px}
.signup .field{flex:1;background:var(--light);font-size:10px;color:var(--muted);padding:7px 12px}
.signup .go{width:60px;background:var(--cyan);display:flex;align-items:center;justify-content:center}
.social-title{margin-top:22px}
.social{display:flex;gap:22px;margin-top:20px;padding-left:6px}
.social span{width:14px;height:14px;border-radius:50%;background:#2d2d2d}
.social span.active{background:var(--cyan)}

.site-footer{position:absolute;left:0;top:2193px;width:1200px;height:49px;background:var(--blue);color:var(--white);font-size:13px;text-align:center;line-height:49px;text-transform:uppercase}
</style>
</head>
<body>

<div class="top-bar">
  <span>Welcome visitor you can login or create an Account</span>
  <div class="account">
    <span>Register for 10% OFF</span>
    <span class="user">
      <svg width="10" height="10" viewBox="0 0 10 10"><circle cx="5" cy="3" r="2.5" fill="#fff"/><path d="M0 10c0-3 2-4.5 5-4.5s5 1.5 5 4.5z" fill="#fff"/></svg>
      Dana Reyes
    </span>
  </div>
</div>

<nav class="site-nav">
  <a class="brand" href="#"><span class="mark"></span>Brisk Tern</a>
  <div class="menu">
    <a class="home" href="#" aria-label="Home">
      <svg width="22" height="20" viewBox="0 0 22 20"><path d="M11 1 1 10h3v9h5v-6h4v6h5v-9h3z" fill="#fff"/></svg>
    </a>
    <a href="#">About</a>
    <a href="#">Product</a>
    <a href="#">Services</a>
    <a href="#">Contact Us</a>
    <a class="search" href="#" aria-label="Search">
      <svg width="15" height="15" viewBox="0 0 15 15"><circle cx="6" cy="6" r="4.5" fill="none" stroke="#1446d8" stroke-width="2"/><path d="M9.5 9.5 14 14" stroke="#1446d8" stroke-width="2.4"/></svg>
    </a>
  </div>
</nav>

<section class="hero" role="img" aria-label="Light aircraft parked on a dark, dramatic studio background">
  <div class="hero-content">
    <h1 class="heading hero-title">Welcome to Brisk Tern</h1>
    <div class="hero-rule"></div>
    <p class="hero-text">Lorem ipsum dolor sit amet, consectetur adipiscing elit, sed do eiusmod<br>tempor incididunt ut labore et dolore magna aliqua.</p>
    <a class="btn-outline" href="#">About Us</a>
  </div>
  <div class="dots"><span class="dot active"></span><span class="dot"></span><span class="dot"></span></div>
</section>

<section class="categories">
  <article class="cat-card">
    <div class="cat-photo formerly" role="img" aria-label="Light aircraft flying at sunset"></div>
    <div class="cat-panel"></div>
    <h2 class="heading cat-title">Aircraft<br>Formerly</h2>
    <p class="cat-text">Lorem ipsum dolor sit amet, consectetur adipiscing elit,</p>
    <a class="cat-more" href="#">Read More &gt;&gt;</a>
  </article>
  <article class="cat-card">
    <div class="cat-photo ultralights" role="img" aria-label="Powered hang glider in flight over countryside"></div>
    <div class="cat-panel"></div>
    <h2 class="heading cat-title">Aircraft<br>Ultralights</h2>
    <p class="cat-text">Lorem ipsum dolor sit amet, consectetur adipiscing elit,</p>
    <a class="cat-more active" href="#">Read More &gt;&gt;</a>
  </article>
  <article class="cat-card">
    <div class="cat-photo microlights" role="img" aria-label="Microlight aircraft above the clouds"></div>
    <div class="cat-panel"></div>
    <h2 class="heading cat-title">Aircraft<br>Microlights</h2>
    <p class="cat-text">Lorem ipsum dolor sit amet, consectetur adipiscing elit,</p>
    <a class="cat-more" href="#">Read More &gt;&gt;</a>
  </article>
</section>
<p class="intro">Lorem ipsum dolor sit amet, consectetur adipiscing elit, sed do eiusmod tempor incididunt ut labore et dolore magna aliqua. Ut enim ad minim veniam, quis nostrud exercitation ullamco laboris nisi ut aliquip ex ea commodo consequat. Duis aute irure dolor in reprehenderit in voluptate velit esse cillum dolore eu fugiat nulla pariatur. Excepteur sint occaecat cupidatat non proident,</p>

<section class="offer">
  <h2 class="heading offer-title">What We Offer</h2>
  <p class="offer-lead">Lorem ipsum dolor sit amet, consectetur adipiscing elit, sed do eiusmod tempor incididunt ut labore et dolore magna aliqua</p>
  <div class="offer-grid">
    <article class="offer-card">
      <svg viewBox="0 0 56 56"><path d="M6 34l8-2 6 4 4-1-5-6 12-4 10 8 6-2c3-1 4-4 1-4l-8 1-12-10-4 1 5 11-11 3-6-4z" fill="#fff"/></svg>
      <h3 class="heading">Commercial</h3>
      <p>Lorem ipsum dolor sit amet, consectetur adipiscing elit, sed do eiusmod tempor incididunt ut laboree magna aliqua. Ut enim ad minim veniam, quis nostrud</p>
    </article>
    <article class="offer-card">
      <svg viewBox="0 0 56 56"><circle cx="28" cy="30" r="14" fill="none" stroke="#fff" stroke-width="5" stroke-dasharray="6 4"/><circle cx="28" cy="30" r="8" fill="#fff"/><circle cx="28" cy="12" r="6" fill="#fff"/></svg>
      <h3 class="heading">Executive</h3>
      <p>Lorem ipsum dolor sit amet, consectetur adipiscing elit, sed do eiusmod tempor incididunt ut laboree magna aliqua. Ut enim ad minim veniam, quis nostrud</p>
    </article>
    <article class="offer-card">
      <svg viewBox="0 0 56 56"><circle cx="34" cy="20" r="9" fill="none" stroke="#fff" stroke-width="6" stroke-dasharray="4 3"/><circle cx="34" cy="20" r="4" fill="#fff"/><circle cx="18" cy="38" r="7" fill="none" stroke="#fff" stroke-width="5" stroke-dasharray="3 3"/><circle cx="18" cy="38" r="3" fill="#fff"/></svg>
      <h3 class="heading">Manufacturer</h3>
      <p>Lorem ipsum dolor sit amet, consectetur adipiscing elit, sed do eiusmod tempor incididunt ut laboree magna aliqua. Ut enim ad minim veniam, quis nostrud</p>
    </article>
  </div>
  <a class="btn-fill" href="#">View More</a>
</section>

<section class="testimonial" role="group" aria-label="Partner testimonial">
  <p class="partner">Aerolume</p>
  <blockquote class="quote">
    <span class="quote-mark open">&ldquo;</span>
    Lorem ipsum dolor sit amet, consectetur adipiscing elit, sed do eiusmod tempor incididunt ut labore et dolore magna aliqua. Ut enim ad minim veniam, quis nostrud exercitation ullamco laboris nisi ut aliquip ex ea commodo consequat. Duis aute irure dolor in reprehenderit in voluptate velit esse cillum dolore eu
    <span class="quote-mark close">&rdquo;</span>
  </blockquote>
  <div class="dots"><span class="dot active"></span><span class="dot"></span><span class="dot"></span></div>
</section>

<section class="bottom">
  <div class="col">
    <h2 class="heading col-title">Lastest News</h2>
    <div class="news-photo" role="img" aria-label="Orange microlight aircraft flying above clouds"></div>
    <p class="news-text"><strong>Lorem ipsum dolor sit amet</strong>, consectetur adipiscing elit, sed do eiusmod tempor incididunt ut labore et dolore magna aliqua. Ut enim ad minim veniam, quis nostrud exercitation ullamco laboris nisi ut aliquip ex ea commodo consequat.</p>
    <a class="btn-fill" href="#">View More</a>
  </div>

  <div class="col">
    <h2 class="heading col-title">Recent Blog Post</h2>
    <article class="post">
      <div class="post-side"><div class="avatar" role="img" aria-label="Author portrait"></div><div class="date"><div class="m">MAY</div><div class="d">03</div></div></div>
      <div><h4>Blog Title Here</h4><p class="by">By: Dana Reyes</p><p>Lorem ipsum dolor sit amet, consectetur adipiscing elit, sed do eiusmod tempor incididunt ut labore et dolore magna aliqua</p><a class="more" href="#">Read More &gt;&gt;</a></div>
    </article>
    <article class="post">
      <div class="post-side"><div class="avatar" role="img" aria-label="Author portrait"></div><div class="date"><div class="m">MAY</div><div class="d">03</div></div></div>
      <div><h4>Blog Title Here</h4><p class="by">By: Dana Reyes</p><p>Lorem ipsum dolor sit amet, consectetur adipiscing elit, sed do eiusmod tempor incididunt ut labore et dolore magna aliqua</p><a class="more" href="#">Read More &gt;&gt;</a></div>
    </article>
    <article class="post">
      <div class="post-side"><div class="avatar" role="img" aria-label="Author portrait"></div><div class="date"><div class="m">MAY</div><div class="d">03</div></div></div>
      <div><h4>Blog Title Here</h4><p class="by">By: Dana Reyes</p><p>Lorem ipsum dolor sit amet, consectetur adipiscing elit, sed do eiusmod tempor incididunt ut labore et dolore magna aliqua</p><a class="more" href="#">Read More &gt;&gt;</a></div>
    </article>
  </div>

  <div class="col">
    <h2 class="heading col-title">Subscribe of our Newsletter</h2>
    <p class="news-join">Join our <span>newsletter</span> and be always up to date!</p>
    <p class="news-small">Lorem ipsum dolor sit amet, consectetur adipiscing elit, sed do eiusmod tempor incididunt ut labore et dolore</p>
    <form class="signup">
      <div class="field">Enter you email adress</div>
      <div class="go"><svg width="8" height="12" viewBox="0 0 8 12"><path d="M1 1l5 5-5 5" fill="none" stroke="#fff" stroke-width="1.6"/></svg></div>
    </form>
    <h2 class="heading col-title social-title">We are Social</h2>
    <div class="social" aria-label="Social links">
      <span></span><span class="active"></span><span></span><span></span><span></span><span></span>
    </div>
  </div>
</section>

<footer class="site-footer">© Copyright 2015 All Rights Reserved.</footer>

</body>
</html>
```